Business Card Design and stationary (thank you cards)

I am basically starting a "handyman" business but have a little ego issue with that term. I have been a professional in the design and construction business for 30 years. I want simple…I will define the scope of work I do as i move forward, and it can vary and i want it to vary.

Target Market(s)

Homeowners mostly

Industry/Entity Type

Business

Contact Information for Business Card

Company Name is "Tidy Corner Crew" Dale P. Whitcombe, 42 Larkvale Hollow Road, Fernhollow, Lv, 06419 (but I may want to use a PO Box), Phone is 860-555-0187, email is dwhitcombe584@mailnest.example,

Font styles to use
Sans Serif

Requirements
Should not have
• anything pre designed….hammers or whatever…custom lines to make home features as shone but simple and elegant

```html
<!DOCTYPE html>
<html lang="en">
<head>
<meta charset="UTF-8">
<title>Tidy Corner Crew – Business Card</title>
<link rel="stylesheet" href="https://fonts.googleapis.com/css2?family=Arimo:wght@400;700&display=swap">
<style>
  :root {
    --page-bg: #e9eaeb;
    --card-dark: #0d0d0d;
    --card-dark-edge: #1e1e1e;
    --card-light: #e4e6e7;
    --card-light-hi: #f2f3f3;
    --ink-light: #ffffff;
    --ink-dark: #1a1a1a;
    --shadow: rgba(0, 0, 0, 0.18);
  }
  html, body {
    margin: 0;
    padding: 0;
    width: 1200px;
    height: 1200px;
    overflow: hidden;
    background: var(--page-bg);
    font-family: "Arimo", Arial, sans-serif;
  }
  .sheet {
    position: relative;
    width: 1200px;
    height: 1200px;
    display: flex;
    flex-direction: column;
    align-items: center;
    justify-content: center;
    gap: 70px;
  }
  .card {
    width: 700px;
    height: 400px;
    box-sizing: border-box;
    box-shadow: 0 10px 28px var(--shadow);
    position: relative;
  }
  .card--front {
    background: linear-gradient(160deg, var(--card-dark-edge) 0%, var(--card-dark) 60%);
    display: flex;
    align-items: center;
    justify-content: center;
  }
  .company-name {
    margin: 0;
    color: var(--ink-light);
    font-weight: 700;
    font-size: 38px;
    letter-spacing: 0.3px;
  }
  .card--back {
    background: radial-gradient(ellipse at 60% 20%, var(--card-light-hi) 0%, var(--card-light) 70%);
    color: var(--ink-dark);
    text-align: center;
  }
  .person-name {
    position: absolute;
    top: 92px;
    left: 0;
    right: 0;
    margin: 0;
    font-weight: 700;
    font-size: 44px;
  }
  .contact {
    position: absolute;
    top: 232px;
    left: 0;
    right: 0;
    margin: 0;
    font-style: normal;
    font-size: 21px;
    line-height: 1.45;
  }
  .contact span { display: block; }
</style>
</head>
<body>
  <main class="sheet">
    <section class="card card--front" aria-label="Card front">
      <h1 class="company-name">Tidy Corner Crew</h1>
    </section>
    <section class="card card--back" aria-label="Card back">
      <h2 class="person-name">Dale P. Whitcombe</h2>
      <address class="contact">
        <span class="contact__address">42 Larkvale Hollow Road, Fernhollow, Lv, 06419</span>
        <span class="contact__phone">Phone: 860-555-0187</span>
        <span class="contact__email">Email: dwhitcombe584@mailnest.example</span>
      </address>
    </section>
  </main>
</body>
</html>
```